post card 4x6

this is a post card that will be sent to plumbing companies and foundation repair companies for whole sale work. if you can add ( work done in unmarked truck -will ware your shirt)

```html
<!DOCTYPE html>
<html lang="en">
<head>
<meta charset="utf-8">
<title>DrainView Wholesale Postcard</title>
<link href="https://fonts.googleapis.com/css2?family=Poppins:wght@400;500;600;700;800&display=swap" rel="stylesheet">
<style>
  :root {
    --navy: #24303f;
    --navy-dark: #1b2431;
    --red: #d12a24;
    --red-dark: #a81c18;
    --white: #ffffff;
    --paper: #ffffff;
    --stage: #ececec;
    --rule: #b9b9b9;
    --stamp: #d6d6d6;
  }
  * { margin: 0; padding: 0; box-sizing: border-box; }
  html, body { width: 1200px; height: 2726px; overflow: hidden; }
  body {
    background: var(--stage);
    font-family: "Poppins", sans-serif;
    position: relative;
  }
  .card {
    position: absolute;
    left: 84px;
    width: 1032px;
    height: 688px;
    background: var(--paper);
    box-shadow: 0 6px 22px rgba(0,0,0,.18);
    overflow: hidden;
  }
  .card-front { top: 637px; }
  .card-back { top: 1400px; }
  .card svg.shapes { position: absolute; inset: 0; }
  .txt { position: absolute; white-space: nowrap; line-height: 1; }

  /* brand */
  .brand { color: var(--red); font-weight: 800; letter-spacing: -1px; }
  .front-brand { left: 55px; top: 42px; font-size: 76px; }
  .back-brand { left: 560px; top: 48px; font-size: 52px; }

  /* front headline */
  .kicker { left: 58px; top: 172px; color: var(--white); font-size: 27px; font-weight: 700; }
  .headline { left: 52px; font-size: 64px; font-weight: 800; letter-spacing: -0.5px; }
  .headline.l1 { top: 202px; color: var(--white); }
  .headline.l2 { top: 264px; color: var(--red); }
  .headline.l3 { top: 326px; color: var(--red); }

  /* service list */
  .svc { color: var(--navy); font-size: 19px; font-weight: 700; display: flex; align-items: center; gap: 8px; }
  .svc .tick { width: 20px; height: 20px; }
  .svc-sub { color: var(--navy); font-size: 18px; font-weight: 400; }
  .svc-sub::before { content: "•"; margin-right: 10px; }
  .list-divider { position: absolute; left: 355px; top: 410px; width: 2px; height: 92px; background: var(--navy); }

  /* slogan */
  .slogan { color: var(--white); font-size: 44px; font-weight: 800; top: 531px; }
  .slogan.make { left: 88px; }
  .slogan.work { left: 532px; }
  .dollar { left: 468px; top: 534px; width: 48px; text-align: center; color: var(--white); font-size: 34px; font-weight: 800; }

  /* front footer */
  .call-label { left: 50px; top: 618px; color: var(--white); font-size: 22px; font-weight: 600; line-height: 1.05; white-space: normal; width: 200px; }
  .front-phone { left: 262px; top: 617px; color: var(--white); font-size: 38px; font-weight: 800; display: flex; align-items: center; gap: 4px; }
  .front-phone svg { width: 28px; height: 28px; }
  .license { left: 596px; top: 597px; color: var(--navy); font-size: 28px; font-weight: 700; }
  .front-web { left: 615px; top: 648px; color: var(--white); font-size: 23px; font-weight: 600; display: flex; align-items: center; gap: 10px; }
  .front-web svg, .back-web svg { width: 24px; height: 24px; }

  /* back */
  .section-title { left: 52px; top: 36px; color: var(--white); font-size: 52px; font-weight: 800; }
  .service-label { color: var(--white); font-size: 22px; font-weight: 400; line-height: 1.15; white-space: normal; width: 240px; }
  .back-call { left: 52px; top: 560px; color: var(--white); font-size: 24px; font-weight: 600; }
  .back-phone { left: 52px; top: 592px; color: var(--white); font-size: 36px; font-weight: 800; display: flex; align-items: center; gap: 10px; }
  .back-phone svg { width: 28px; height: 28px; }
  .back-web { left: 52px; top: 636px; color: var(--white); font-size: 28px; font-weight: 600; display: flex; align-items: center; gap: 10px; }
  .stamp-box { position: absolute; left: 855px; top: 45px; width: 125px; height: 125px; background: var(--stamp); }
  .address-line { position: absolute; left: 645px; width: 325px; height: 1px; background: var(--rule); }
</style>
</head>
<body>

<!-- FRONT -->
<section class="card card-front">
  <svg class="shapes" viewBox="0 0 1032 688" width="1032" height="688">
    <defs>
      <linearGradient id="g-hands" x1="0" y1="0" x2="1" y2="1">
        <stop offset="0" stop-color="#d9dde2"/>
        <stop offset=".5" stop-color="#9aa3ad"/>
        <stop offset="1" stop-color="#e8e8e8"/>
      </linearGradient>
      <radialGradient id="g-pipe-blue" cx=".5" cy=".5" r=".6">
        <stop offset="0" stop-color="#1a2030"/>
        <stop offset=".4" stop-color="#4c6a8f"/>
        <stop offset="1" stop-color="#2a3140"/>
      </radialGradient>
      <radialGradient id="g-pipe-amber" cx=".5" cy=".5" r=".6">
        <stop offset="0" stop-color="#221510"/>
        <stop offset=".45" stop-color="#c8662a"/>
        <stop offset="1" stop-color="#3a2620"/>
      </radialGradient>
    </defs>
    <!-- navy headline band -->
    <rect x="0" y="137" width="640" height="263" fill="var(--navy)"/>
    <rect x="600" y="345" width="432" height="55" fill="var(--navy)"/>
    <!-- red chevron edge -->
    <polygon points="590,0 625,0 545,190 655,390 620,390 510,190" fill="var(--red)"/>
    <!-- main photo -->
    <polygon points="615,0 1032,0 1032,345 645,345 545,190" fill="url(#g-hands)" role="img" aria-label="Gloved hands tightening a chrome drain pipe with a red pipe wrench"/>
    <!-- lower photos -->
    <polygon points="620,490 760,490 812,345 672,345" fill="url(#g-pipe-blue)" role="img" aria-label="Sewer camera view inside a dark pipe"/>
    <polygon points="772,490 785,490 837,345 824,345" fill="var(--red)"/>
    <polygon points="795,490 975,490 1027,345 847,345" fill="url(#g-pipe-amber)" role="img" aria-label="Inspection camera view of a lit pipe interior"/>
    <polygon points="985,490 998,490 1032,395 1032,358" fill="var(--red)"/>
    <!-- slogan bars -->
    <polygon points="72,530 450,530 438,580 55,580" fill="var(--navy-dark)"/>
    <polygon points="505,530 963,530 943,580 490,580" fill="var(--red)"/>
    <circle cx="492" cy="555" r="28" fill="var(--navy-dark)" stroke="var(--red)" stroke-width="4"/>
    <!-- footer -->
    <polygon points="0,594 590,594 620,688 0,688" fill="var(--red)"/>
    <polygon points="602,636 1032,636 1032,688 624,688" fill="var(--white)"/>
    <polygon points="612,640 1032,640 1032,688 634,688" fill="var(--navy)"/>
  </svg>

  <div class="txt brand front-brand">DrainView</div>

  <div class="txt kicker">YOUR ONE-STOP SOLUTION FOR</div>
  <div class="txt headline l1">PLUMBING &amp;</div>
  <div class="txt headline l2">IRRIGATION</div>
  <div class="txt headline l3">INSTALLATION</div>

  <div class="txt svc" style="left:50px;top:412px;">
    <svg class="tick" viewBox="0 0 20 20"><circle cx="10" cy="10" r="8.5" fill="none" stroke="var(--red)" stroke-width="1.6"/><path d="M6 10.3l2.6 2.6L14 7.5" fill="none" stroke="var(--red)" stroke-width="1.8"/></svg>
    CIPP (CURED IN PLACE PIPE)
  </div>
  <div class="txt svc" style="left:50px;top:438px;">
    <svg class="tick" viewBox="0 0 20 20"><circle cx="10" cy="10" r="8.5" fill="none" stroke="var(--red)" stroke-width="1.6"/><path d="M6 10.3l2.6 2.6L14 7.5" fill="none" stroke="var(--red)" stroke-width="1.8"/></svg>
    SIPP (SPRAY IN PLACE PIPE)
  </div>
  <div class="txt svc-sub" style="left:82px;top:466px;">PIPE BURSTING</div>
  <div class="txt svc-sub" style="left:82px;top:489px;">HYDRO JETTING</div>
  <div class="list-divider"></div>
  <div class="txt svc" style="left:362px;top:412px;align-items:flex-start;">
    <svg class="tick" viewBox="0 0 20 20"><circle cx="10" cy="10" r="8.5" fill="none" stroke="var(--red)" stroke-width="1.6"/><path d="M6 10.3l2.6 2.6L14 7.5" fill="none" stroke="var(--red)" stroke-width="1.8"/></svg>
    <span style="line-height:1.15;">SEWER CAMERA<br>AND LOCATE</span>
  </div>
  <div class="txt svc-sub" style="left:388px;top:466px;">RESIZE CAST IRON</div>

  <div class="txt slogan make">YOU MAKE THE</div>
  <div class="txt dollar">$</div>
  <div class="txt slogan work">WE DO THE WORK</div>

  <div class="txt call-label">CALL FOR WHOLE SALE PRICING</div>
  <div class="txt front-phone">
    <svg viewBox="0 0 24 24"><path d="M6.6 10.8a15 15 0 0 0 6.6 6.6l2.2-2.2a1 1 0 0 1 1-.25 11.4 11.4 0 0 0 3.6.57 1 1 0 0 1 1 1V20a1 1 0 0 1-1 1A17 17 0 0 1 3 4a1 1 0 0 1 1-1h3.5a1 1 0 0 1 1 1c0 1.25.2 2.45.57 3.6a1 1 0 0 1-.25 1z" fill="var(--white)"/></svg>
    555-014-2290
  </div>
  <div class="txt license">RMP#20871</div>
  <div class="txt front-web">
    <svg viewBox="0 0 24 24"><circle cx="12" cy="12" r="9" fill="none" stroke="var(--red)" stroke-width="2"/><path d="M3 12h18M12 3c3 3 3 15 0 18M12 3c-3 3-3 15 0 18" fill="none" stroke="var(--red)" stroke-width="1.6"/></svg>
    www.drainviewpipeworks.com
  </div>
</section>

<!-- BACK -->
<section class="card card-back">
  <svg class="shapes" viewBox="0 0 1032 688" width="1032" height="688">
    <defs>
      <linearGradient id="g-tech" x1="0" y1="0" x2="1" y2="1"><stop offset="0" stop-color="#8a6a4a"/><stop offset="1" stop-color="#4f6d8c"/></linearGradient>
      <linearGradient id="g-burst" x1="0" y1="0" x2="1" y2="1"><stop offset="0" stop-color="#4a3f36"/><stop offset="1" stop-color="#a9acb0"/></linearGradient>
      <linearGradient id="g-jet" x1="0" y1="0" x2="1" y2="1"><stop offset="0" stop-color="#6b5545"/><stop offset="1" stop-color="#dcdcdc"/></linearGradient>
      <linearGradient id="g-lining" x1="0" y1="0" x2="1" y2="1"><stop offset="0" stop-color="#e8e2da"/><stop offset="1" stop-color="#3b4a66"/></linearGradient>
    </defs>
    <polygon points="465,0 492,0 605,330 520,550 493,550 578,330" fill="var(--red)"/>
    <polygon points="0,0 465,0 490,120 0,120" fill="var(--red)"/>
    <polygon points="0,120 490,120 578,330 493,550 0,550" fill="var(--navy)"/>
    <polygon points="0,550 493,550 585,688 0,688" fill="var(--red)"/>
    <line x1="295" y1="140" x2="295" y2="525" stroke="#3a4657" stroke-width="2"/>

    <circle cx="140" cy="206" r="72" fill="var(--white)"/>
    <circle cx="140" cy="206" r="68" fill="var(--red)"/>
    <circle cx="140" cy="206" r="63" fill="url(#g-tech)" role="img" aria-label="Technician cleaning a drain under a cabinet with a drain machine"/>

    <circle cx="393" cy="206" r="72" fill="var(--white)"/>
    <circle cx="393" cy="206" r="68" fill="var(--red)"/>
    <circle cx="393" cy="206" r="63" fill="url(#g-burst)" role="img" aria-label="Pipe bursting head in a dug trench"/>

    <circle cx="140" cy="428" r="72" fill="var(--white)"/>
    <circle cx="140" cy="428" r="68" fill="var(--red)"/>
    <circle cx="140" cy="428" r="63" fill="url(#g-jet)" role="img" aria-label="Cut section of old pipe beside a new lined pipe"/>

    <circle cx="393" cy="428" r="72" fill="var(--white)"/>
    <circle cx="393" cy="428" r="68" fill="var(--red)"/>
    <circle cx="393" cy="428" r="63" fill="url(#g-lining)" role="img" aria-label="Technician operating pipe lining equipment"/>
  </svg>

  <div class="txt section-title">OUR SERVICES</div>
  <div class="txt service-label" style="left:63px;top:285px;">Drain and Pipe<br>Repair and Cleaning</div>
  <div class="txt service-label" style="left:343px;top:288px;">Pipe<br>Bursting</div>
  <div class="txt service-label" style="left:63px;top:515px;">Hydro Jetting</div>
  <div class="txt service-label" style="left:343px;top:518px;">Pipe Lining</div>

  <div class="txt back-call">CALL FOR WHOLE SALE PRICING</div>
  <div class="txt back-phone">
    <svg viewBox="0 0 24 24"><path d="M6.6 10.8a15 15 0 0 0 6.6 6.6l2.2-2.2a1 1 0 0 1 1-.25 11.4 11.4 0 0 0 3.6.57 1 1 0 0 1 1 1V20a1 1 0 0 1-1 1A17 17 0 0 1 3 4a1 1 0 0 1 1-1h3.5a1 1 0 0 1 1 1c0 1.25.2 2.45.57 3.6a1 1 0 0 1-.25 1z" fill="var(--white)"/></svg>
    555-014-2290
  </div>
  <div class="txt back-web">
    <svg viewBox="0 0 24 24"><circle cx="12" cy="12" r="9" fill="none" stroke="var(--white)" stroke-width="2"/><path d="M3 12h18M12 3c3 3 3 15 0 18M12 3c-3 3-3 15 0 18" fill="none" stroke="var(--white)" stroke-width="1.6"/></svg>
    www.drainviewpipeworks.com
  </div>

  <div class="txt brand back-brand">DrainView</div>
  <div class="stamp-box"></div>
  <div class="address-line" style="top:305px;"></div>
  <div class="address-line" style="top:363px;"></div>
  <div class="address-line" style="top:413px;"></div>
  <div class="address-line" style="top:470px;"></div>
</section>

</body>
</html>
```